Packaging & Label Design for CDB Products

We are a European CBD company specialising in athletic recovery, sleep improvement and wellness.

We would like the packaging to incorporate our logo and name (and font 'Codec') 'Meridell CBD'. The design must be transferable to all of our products. CBD Oils, Balms, Lip Balm and Vape E-Liquid.

We would like it to be simple but eye-catching and modern. We don't want bright colours. Preferred pallet of muted greys, blacks, white and pastel colours. Geometric concepts, possibly using different colours for each item of the range, we are open to new and fresh ideas (we are seeking you for your experience) and when we find the right design we would likely throw more work in your direction..

Our product range is not complete so the designer must be flexible with some changes and provide files where format can be easily edited by packaging manufacturer. We are also waiting for dimensions for the labels and boxes for several products and will supply the designer with full dimensions of all products once selected.

Oil Box: 2.6 x 9.0 x 2.6 cm (open format 16.7 x 11.6cm)
Labels: 7.8 x 3.3 cm (Front and Back)

Our expected product range will be:
CBD Oil 1000mg
CBD Oil 3000mg
CBD Balm 100mg
CBD Balm 300mg
E-Liquid 500mg
Lip Balm 50mg

We look forward to seeing your ideas.

Best Regards
Meridell CBD

```html
<!DOCTYPE html>
<html lang="en">
<head>
<meta charset="UTF-8">
<title>Meridell CBD – CBD Oil Packaging</title>
<link rel="stylesheet" href="https://fonts.googleapis.com/css2?family=Montserrat:wght@700&family=Roboto+Condensed:wght@400;500&family=Roboto:wght@400&display=swap">
<style>
  :root {
    --canvas: #e9e7e4;
    --charcoal: #3a3b3c;
    --charcoal-deep: #2f3031;
    --paper: #f7f7f7;
    --paper-shade: #e4e4e4;
    --ink: #1e1f20;
    --mint: #b4d6c4;
    --mint-light: #c9e4d6;
    --muted: #d6d6d6;
  }
  * { margin: 0; padding: 0; box-sizing: border-box; }
  html, body {
    width: 1200px; height: 800px; overflow: hidden;
    background: var(--canvas);
  }
  .stage { position: relative; width: 1200px; height: 800px; }

  .panel {
    position: absolute;
    overflow: hidden;
    background: linear-gradient(90deg, var(--paper-shade), var(--paper) 30%, var(--paper) 70%, var(--paper-shade));
  }
  .box-front { left: 300px; top: 120px; width: 290px; height: 560px; }
  .bottle-label { left: 660px; top: 230px; width: 230px; height: 340px; }

  .band-top {
    position: absolute; left: 0; top: 0; width: 100%; height: 36px;
    background: var(--charcoal);
  }
  .band-bottom {
    position: absolute; left: 0; bottom: 0; width: 100%;
    background: linear-gradient(180deg, var(--charcoal), var(--charcoal-deep));
  }
  .box-front .band-bottom { height: 260px; }
  .bottle-label .band-bottom { height: 120px; }

  .brand {
    position: absolute; left: 0; width: 100%;
    display: flex; align-items: center; justify-content: center; gap: 10px;
    font-family: "Montserrat", sans-serif; font-weight: 700;
    color: var(--ink); letter-spacing: 0.04em;
  }
  .brand-dot { border-radius: 50%; background: var(--ink); }
  .box-front .brand { top: 150px; font-size: 24px; }
  .box-front .brand-dot { width: 14px; height: 14px; }
  .bottle-label .brand { top: 78px; font-size: 19px; }
  .bottle-label .brand-dot { width: 11px; height: 11px; }

  .potency { position: absolute; }
  .potency svg { position: absolute; left: 0; top: 0; width: 100%; height: 100%; }
  .potency-text {
    position: absolute; right: 26px; top: 22px; text-align: right;
    font-family: "Roboto Condensed", sans-serif; color: var(--ink); line-height: 1;
  }
  .product { display: block; font-weight: 500; }
  .strength { display: block; font-weight: 400; margin-top: 6px; }

  .box-front .potency { left: 64px; top: 235px; width: 226px; height: 118px; }
  .box-front .product { font-size: 46px; }
  .box-front .strength { font-size: 23px; }

  .bottle-label .potency { left: 46px; top: 158px; width: 184px; height: 100px; }
  .bottle-label .potency-text { right: 22px; top: 18px; }
  .bottle-label .product { font-size: 38px; }
  .bottle-label .strength { font-size: 19px; margin-top: 5px; }

  .volume {
    position: absolute; left: 0; width: 100%; text-align: center;
    font-family: "Roboto", sans-serif; color: var(--muted);
  }
  .box-front .volume { bottom: 30px; font-size: 15px; }
  .bottle-label .volume { bottom: 22px; font-size: 13px; }
</style>
</head>
<body>
<main class="stage">

  <section class="panel box-front" aria-label="Carton front panel">
    <div class="band-top"></div>
    <div class="band-bottom"></div>
    <div class="brand"><span class="brand-dot"></span>Meridell CBD</div>
    <div class="potency">
      <svg viewBox="0 0 226 118" preserveAspectRatio="none" aria-hidden="true">
        <defs>
          <linearGradient id="mintBox" x1="0" y1="0" x2="1" y2="1">
            <stop offset="0" stop-color="var(--mint-light)"/>
            <stop offset="1" stop-color="var(--mint)"/>
          </linearGradient>
        </defs>
        <path d="M28,22 C70,2 190,-4 214,26 C232,52 222,100 186,110 C146,120 116,86 62,101 C22,112 2,88 5,60 C7,42 14,30 28,22Z"
              fill="url(#mintBox)" stroke="#f3f3f3" stroke-width="4"/>
      </svg>
      <div class="potency-text">
        <span class="product">CBD OIL</span>
        <span class="strength">1000 mg</span>
      </div>
    </div>
    <p class="volume">1 fl oz. ( 30ml )</p>
  </section>

  <section class="panel bottle-label" aria-label="Bottle front label">
    <div class="band-bottom"></div>
    <div class="brand"><span class="brand-dot"></span>Meridell CBD</div>
    <div class="potency">
      <svg viewBox="0 0 226 118" preserveAspectRatio="none" aria-hidden="true">
        <defs>
          <linearGradient id="mintLabel" x1="0" y1="0" x2="1" y2="1">
            <stop offset="0" stop-color="var(--mint-light)"/>
            <stop offset="1" stop-color="var(--mint)"/>
          </linearGradient>
        </defs>
        <path d="M28,22 C70,2 190,-4 214,26 C232,52 222,100 186,110 C146,120 116,86 62,101 C22,112 2,88 5,60 C7,42 14,30 28,22Z"
              fill="url(#mintLabel)" stroke="#f3f3f3" stroke-width="4"/>
      </svg>
      <div class="potency-text">
        <span class="product">CBD OIL</span>
        <span class="strength">1000 mg</span>
      </div>
    </div>
    <p class="volume">1 fl oz. ( 30ml )</p>
  </section>

</main>
</body>
</html>
```